GUARANTEED WordPress design needed for a sassy, confident charisma coach!

We need a website design for Marla Penrick's brand new, responsive, Wordpress website.
Marla is a trainer / coach who teaches people how to be more charismatic and runs events, publishes video courses and has an ongoing video blog. Her old website is here: www.marlapenrick.co.uk ... but it's now time to have a much better site!
We have a strong idea about the technical components of the website, but we need a designer's eye to create a great style for the site (and provide layered PSD files which our developers will then convert to HTML and CSS).
Marla's brand is sassy, brave, warm and confident. The videos on her existing site give quite a good feel for her personality. We need a clean, stylish and compelling page that isn't too corporate and captures her personality. Every element needs to feel coherent, from fonts and headings to colours and spacing.
The following sites are not exactly what Marla wants (and certainly aren't right in terms of colours) but they give you an idea of the kind of people she is competing against and the area she is operating in:
http://www.tessa-broughley.example/
http://rowanfelsby.example/
Ideally, you will have done something similar and be able to key in on exactly the kind of thing we want: we're not looking to reinvent the wheel. Hopefully you won't mind tweaking a few things if you are close to what we need.
More detail is provided in the word document attached. But in a nutshell we need: a banner, footer, sign-up strap, menu bar, signature and 4 different basic page types. We want bursts of bright colours, contrasted with black and white if possible - sorry we can't be more specific than that...
The word doc also contains some amateur mock-ups as well (the images are also just mockups at this stage) - but although these give a general sense of the structure what we are looking for, we are clearly not designers...so please help! We need a designer's touch!
Kind regards,
Corin
PS The layered PSD versions of the mockup files are available on Cloudvantre: https://files.cloudvantre.example/sh/k72pqa4w1zbtmrd/QXvenlr8Ty3PwMiU6Hs2kYfDb?dl=0
Target Market(s)
Entrepreneurs who need to sell themselves.
Number of Pages Required
4 page

```html
<!DOCTYPE html>
<html lang="en">
<head>
<meta charset="utf-8">
<title>Marla Penrick – Charisma Coach</title>
<link href="https://fonts.googleapis.com/css2?family=Open+Sans:wght@300;400;600;700&family=Roboto:wght@300;400;700;900&family=Playfair+Display:wght@700;900&family=Lato:wght@400;700&display=swap" rel="stylesheet">
<style>
:root{
  --slate:#4b5a6e;
  --slate-dark:#2e3b4c;
  --nav:#56687f;
  --nav-active:#2b3746;
  --hero-a:#1f2b3a;
  --hero-b:#55677d;
  --accent:#f0452a;
  --accent-dark:#d8381f;
  --yellow:#ffe21a;
  --page:#f2f2f2;
  --card:#ffffff;
  --ink:#333;
  --muted:#666;
  --sky:#8fb1d6;
  --white:#fff;
}
*{box-sizing:border-box;margin:0;padding:0}
html,body{width:1200px;height:2812px;overflow:hidden}
body{position:relative;background:var(--page);font-family:"Open Sans",Arial,sans-serif;color:var(--ink)}
.abs{position:absolute}

/* top bar */
.topbar{left:0;top:0;width:1200px;height:66px;background:var(--nav);border-bottom:1px solid #3c4a5c}
.brand{left:222px;top:12px;font-family:"Open Sans",sans-serif;font-weight:600;font-size:32px;color:var(--white);letter-spacing:.5px}
.menu{left:470px;top:0;height:66px;display:flex;list-style:none}
.menu li{width:106px;height:66px;display:flex;align-items:center;justify-content:center;font-family:"Open Sans",sans-serif;font-weight:700;font-size:11.5px;color:var(--white);border-left:1px solid #46576c;text-transform:uppercase}
.menu li.active{background:var(--nav-active)}

/* hero */
.hero{left:0;top:66px;width:1200px;height:324px;background:radial-gradient(ellipse at 55% 40%,var(--hero-b),var(--hero-a) 80%)}
.hero-title{left:264px;top:148px;font-family:"Playfair Display",serif;font-weight:900;font-size:60px;line-height:.6;color:var(--white);z-index:2}
.hero-title span{display:block;height:38px}
.hero-title .connect{color:var(--sky);padding-left:92px}
.hero-portrait{left:600px;top:66px;width:300px;height:324px;background:linear-gradient(180deg,#5a4a48 0%,#c73a3a 35%,#e23b3b 70%,#b8302f 100%);border-radius:140px 140px 0 0}

/* sign-up strap */
.strap{left:0;top:390px;width:1200px;height:136px;background:var(--slate)}
.video-screen{left:253px;top:338px;width:207px;height:140px;background:linear-gradient(135deg,#3a3a3a,#c9c9c9 40%,#b83030 75%,#2a2a2a);border:7px solid #222;border-radius:6px}
.video-stand{left:330px;top:478px;width:54px;height:24px;background:#cfd3d8;clip-path:polygon(25% 0,75% 0,100% 100%,0 100%)}
.strap-copy{left:478px;top:410px;width:470px;font-family:"Roboto",sans-serif;font-size:16.5px;line-height:22px;color:var(--white)}
.strap-copy strong{color:var(--yellow);font-weight:700}
.field{height:30px;background:var(--white);border-radius:16px;font-family:"Open Sans",sans-serif;font-size:11px;color:#555;padding:8px 18px}
.btn{height:30px;background:var(--accent);border-radius:16px;font-family:"Open Sans",sans-serif;font-weight:700;font-size:10.5px;color:var(--white);display:flex;align-items:center;justify-content:center;text-transform:uppercase}
.strap-note{left:478px;top:500px;width:500px;text-align:center;font-size:8.5px;color:#d8dde4}

/* posts */
.post{left:199px;width:532px;height:444px;background:var(--card);box-shadow:0 2px 5px rgba(0,0,0,.22)}
.post-banner{position:absolute;left:35px;top:35px;width:460px;height:222px;overflow:hidden}
.post-banner .words{position:absolute;left:42px;z-index:2;font-family:"Roboto",sans-serif;color:var(--white);font-size:32px;line-height:32px;text-transform:uppercase}
.words .lt{font-weight:300}
.words .bd{font-weight:700}
.post-banner .person{position:absolute;right:16px;bottom:0;width:100px;height:200px;border-radius:50px 50px 0 0;z-index:1}
.post-title{position:absolute;left:38px;top:276px;width:460px;font-family:"Open Sans",sans-serif;font-weight:300;font-size:25px;color:#555;white-space:nowrap}
.post-title.small{font-size:20px;top:280px;font-weight:400}
.post-excerpt{position:absolute;left:38px;top:310px;width:460px;font-size:12.2px;line-height:15px;color:#666}
.read-more{position:absolute;left:38px;top:392px;font-size:10px;color:var(--accent);text-transform:uppercase}

.b-red{background:linear-gradient(90deg,#e0503e,#c8402f)}
.b-blue{background:linear-gradient(90deg,#4256c4,#2f3f9c)}
.b-slate{background:linear-gradient(90deg,#3f4d5a,#2f3a45)}
.b-tan{background:linear-gradient(90deg,#b19a78,#8c7658)}

/* sidebar */
.sidebar{left:750px;top:557px;width:250px;height:1836px;background:var(--card);box-shadow:0 2px 5px rgba(0,0,0,.22)}
.side-head{position:absolute;left:0;width:250px;text-align:center;font-family:"Lato",sans-serif;font-weight:700;font-size:23px;color:#111;text-transform:uppercase}
.side-sub{position:absolute;left:0;width:250px;text-align:center;font-size:11px;color:var(--accent);text-transform:uppercase}
.popular{position:absolute;left:21px;top:82px;width:210px;list-style:none}
.popular li{border-bottom:1px solid #e2e2e2;text-align:center;font-size:9.5px;line-height:12px;color:#222;padding:6px 6px 4px;height:58px}
.popular li span{display:block;color:var(--accent);font-size:8.5px;margin-top:7px}
.tags{position:absolute;left:21px;top:376px;width:210px;display:flex;flex-wrap:wrap;justify-content:center;gap:3px 3px}
.tag{color:var(--white);font-size:9.5px;padding:2px 4px;line-height:13px}
.tag.lg{font-size:18px;line-height:21px;padding:1px 4px}
.tag.md{font-size:14px;line-height:18px}
.t-red{background:#e0706a}.t-teal{background:#5eb2a8}.t-gray{background:#8c8c8c}.t-rose{background:#d99ca4}
.t-olive{background:#b8b065}.t-lav{background:#9d9bc8}.t-purple{background:#7a78c0}.t-mint{background:#7fcac4}.t-khaki{background:#a9a272}
.promo{position:absolute;left:21px;top:619px;width:210px;height:448px;background:linear-gradient(180deg,#2a2a2a 0%,#4a4644 35%,#6d625a 70%,#3a3432 100%);font-family:"Roboto",sans-serif;color:var(--white);text-align:center}
.promo-title{position:absolute;left:0;top:22px;width:210px;font-weight:700;font-size:24px;line-height:28px;text-transform:uppercase}
.promo-live{position:absolute;left:0;top:198px;width:210px;font-weight:900;font-size:60px;color:var(--accent);text-transform:uppercase}
.promo-places{position:absolute;left:0;top:308px;width:210px;font-weight:700;font-size:20px;line-height:24px}
.promo-btn{position:absolute;left:0;bottom:16px;width:210px;height:52px;background:var(--accent);display:flex;align-items:center;justify-content:center;font-weight:700;font-size:17px;text-transform:uppercase}

/* pagination */
.pager{left:376px;top:2420px;display:flex;gap:12px;list-style:none}
.pager li{width:20px;height:20px;border-radius:50%;background:#e3e3e3;font-size:9px;color:#555;display:flex;align-items:center;justify-content:center}
.pager li.current{background:var(--accent);color:var(--white)}
.pager li.next{background:#555;color:var(--white)}

/* footer */
.footer{left:0;top:2490px;width:1200px;height:322px;background:var(--slate)}
.footer-pitch{left:0;top:2538px;width:1200px;text-align:center;font-family:"Roboto",sans-serif;font-size:21px;line-height:27px;color:var(--white)}
.footer-sad{left:0;top:2672px;width:1200px;text-align:center;font-family:"Roboto",sans-serif;font-weight:300;font-size:36px;color:#dfe4ea}
.social{left:506px;top:2726px;display:flex;gap:6px}
.social span{width:32px;height:32px;border-radius:50%;background:#2b8fcf;border:2px solid var(--white)}
.social span:nth-child(4){background:#d2302c}
.legal{left:0;top:2779px;width:1200px;display:flex;justify-content:center;font-size:9.5px;color:#d8dde4;text-transform:uppercase}
.legal span{padding:0 22px;border-left:1px solid #8a96a6}
.legal span:first-child{border-left:0;text-transform:none}
</style>
</head>
<body>

<header class="abs topbar"></header>
<div class="abs brand">Marla Penrick</div>
<ul class="abs menu">
  <li>Events</li><li>Work with me</li><li class="active">Corporate</li><li>About</li><li>Contact</li>
</ul>

<section class="abs hero" role="img" aria-label="Dark blue textured backdrop"></section>
<div class="abs hero-portrait" role="img" aria-label="Photo of Marla standing confidently in a red dress, hands on hips"></div>
<h1 class="abs hero-title"><span>Attract</span><span class="connect">Connect</span><span>Influence</span></h1>

<section class="abs strap"></section>
<div class="abs video-screen" role="img" aria-label="Computer screen showing a still from Marla's free training video"></div>
<div class="abs video-stand"></div>
<p class="abs strap-copy">Learn how to unlock the superpower* of your charisma and win all the business you want with this <strong>FREE training.</strong></p>
<div class="abs field" style="left:480px;top:465px;width:188px">First name</div>
<div class="abs field" style="left:671px;top:465px;width:188px">Email address</div>
<div class="abs btn" style="left:866px;top:465px;width:111px">Yes please!</div>
<p class="abs strap-note">* Promise to only use your powers for good</p>

<article class="abs post" style="top:557px">
  <div class="post-banner b-red">
    <div class="words" style="top:45px"><span class="lt">Public</span><br><span class="bd">Speaking...</span><br><span class="lt">Made </span><span class="bd">Easy :-)</span></div>
    <div class="person" style="background:linear-gradient(180deg,#6b3a32,#e8493b)" role="img" aria-label="Photo of Marla speaking on stage"></div>
  </div>
  <h2 class="post-title">Public speaking...made easy</h2>
  <p class="post-excerpt">Lorem ipsum dolor sit amet, consectetur adipiscing elit. Praesent fringilla tortor et mi convallis, ut scelerisque dui rhoncus. Donec quis lorem malesuada, molestie metus id, vehicula lacus. Pellentesque ultricies venenatis ullamcorper. Sed metus ligula, pharetra id risus eu, fermentum auctor eros.</p>
  <span class="read-more">Keep reading ►</span>
</article>

<article class="abs post" style="top:1020px">
  <div class="post-banner b-blue">
    <div class="words" style="top:42px"><span class="lt">How to start</span><br><span class="bd">Every day</span><br><span class="lt">In the right</span><br><span class="bd">Frame of mind!</span></div>
    <div class="person" style="background:linear-gradient(180deg,#3a2f36,#2a3c9a)" role="img" aria-label="Photo of Marla talking to camera"></div>
  </div>
  <h2 class="post-title">How to start every day in the right</h2>
  <p class="post-excerpt">Lorem ipsum dolor sit amet, consectetur adipiscing elit. Praesent fringilla tortor et mi convallis, ut scelerisque dui rhoncus. Donec quis lorem malesuada, molestie metus id, vehicula lacus. Pellentesque ultricies venenatis ullamcorper. Sed metus ligula, pharetra id risus eu, fermentum auctor eros.</p>
  <span class="read-more">Keep reading ►</span>
</article>

<article class="abs post" style="top:1485px">
  <div class="post-banner b-slate">
    <div class="words" style="top:42px"><span class="lt">Take charge of</span><br><span class="bd">Your style...</span><br><span class="lt">...Boost your</span><br><span class="bd">Confidence</span></div>
    <div class="person" style="width:140px;height:150px;border-radius:0;background:linear-gradient(135deg,#f4f4f4,#e9b3b3)" role="img" aria-label="Style tips card with a red dress, shoes and Marla's photo"></div>
  </div>
  <h2 class="post-title small">Take charge of your style...Boost your confidence</h2>
  <p class="post-excerpt">Lorem ipsum dolor sit amet, consectetur adipiscing elit. Praesent fringilla tortor et mi convallis, ut scelerisque dui rhoncus. Donec quis lorem malesuada, molestie metus id, vehicula lacus. Pellentesque ultricies venenatis ullamcorper. Sed metus ligula, pharetra id risus eu, fermentum auctor eros.</p>
  <span class="read-more">Keep reading ►</span>
</article>

<article class="abs post" style="top:1950px">
  <div class="post-banner b-tan">
    <div class="words" style="top:26px;left:34px;font-size:27px;line-height:27px"><span class="lt">Unfulfilled?</span><br><span class="bd">It's time to think<br>about your values...</span><br><span class="lt">Do this</span><br><span class="bd">Exercise now!</span></div>
    <div class="person" style="width:80px;right:10px;border-radius:40px 40px 0 0;background:linear-gradient(180deg,#3a302a,#6a5a4a)" role="img" aria-label="Photo of Marla presenting"></div>
  </div>
  <h2 class="post-title small">Unfulfilled? It's time to think about your values...</h2>
  <p class="post-excerpt">Lorem ipsum dolor sit amet, consectetur adipiscing elit. Praesent fringilla tortor et mi convallis, ut scelerisque dui rhoncus. Donec quis lorem malesuada, molestie metus id, vehicula lacus. Pellentesque ultricies venenatis ullamcorper. Sed metus ligula, pharetra id risus eu, fermentum auctor eros.</p>
  <span class="read-more">Keep reading ►</span>
</article>

<aside class="abs sidebar">
  <h3 class="side-head" style="top:26px">Marla says...</h3>
  <p class="side-sub" style="top:62px">Popular</p>
  <ul class="popular">
    <li>Be more dog: 5 lessons we could learn from our best friends<span>13/07/16</span></li>
    <li>Are you letting your core beliefs hold you back?<span>06/07/16</span></li>
    <li>How I learned to stop worrying and start NETWORKING!<span>30/06/16</span></li>
    <li>Bitchy resting face and other strange - but true - problems<span>23/06/16</span></li>
  </ul>
  <p class="side-sub" style="top:355px;color:#333;font-size:10px">Tags</p>
  <div class="tags">
    <span class="tag t-red">body language</span>
    <span class="tag lg t-teal">capsule wardrobe</span>
    <span class="tag t-teal">confidence</span><span class="tag t-gray">handshake</span><span class="tag t-red">mindset</span><span class="tag t-lav">nlp</span>
    <span class="tag t-rose">passion</span><span class="tag md t-olive">power pose</span>
    <span class="tag t-purple">presentations</span><span class="tag t-mint">presence</span>
    <span class="tag lg t-khaki">rapport</span><span class="tag t-olive">spring wear</span><span class="tag t-gray">style</span>
    <span class="tag t-gray">values</span><span class="tag t-lav">vision board</span><span class="tag t-red">warmth</span>
  </div>
  <h3 class="side-head" style="top:582px">Coming up</h3>
  <div class="promo" role="img" aria-label="Photo of Marla coaching a live workshop audience">
    <div class="promo-title">Unlock the<br>superpower<br>of charisma</div>
    <div class="promo-live">Live</div>
    <div class="promo-places">* Only 6<br>places left.</div>
    <div class="promo-btn">Learn more</div>
  </div>
</aside>

<ul class="abs pager">
  <li class="current">1</li><li>2</li><li>3</li><li>..</li><li>15</li><li class="next">»</li>
</ul>

<footer class="abs footer"></footer>
<p class="abs footer-pitch">Hey! Don't go without signing up because you'll miss out on exclusive offers,<br>awesome tips, and weekly motivation in my fab newsletter *.</p>
<div class="abs field" style="left:362px;top:2614px;width:187px">First name</div>
<div class="abs field" style="left:555px;top:2614px;width:187px">Email address</div>
<div class="abs btn" style="left:750px;top:2614px;width:109px">Yes please!</div>
<p class="abs footer-sad">* And that'll make me sad</p>
<div class="abs social" aria-label="Social links"><span></span><span></span><span></span><span></span><span></span></div>
<div class="abs legal"><span>© 2016 Marla Penrick Ltd</span><span>Privacy policy</span><span>Terms policy</span><span>Disclaimers</span></div>

</body>
</html>
```